Kestrel Builders Business Card Design Project

Clean sharp business card
Ability to write on back of card
Details for the card -
Address: PO Box 5867, Wendara, NSW, 2487
ABN: 47 305 961 220
BSA LIC 2650874
Ph: 07 3562 4470
Fax: 07 3562 4475
Email: kestrelbuilders@mailbrook.com.au

```html
<!DOCTYPE html>
<html lang="en">
<head>
<meta charset="UTF-8">
<title>Kestrel Builders – Business Card</title>
<link href="https://fonts.googleapis.com/css2?family=Arimo:wght@400;700&display=swap" rel="stylesheet">
<style>
  :root {
    --backdrop: #6f6b7b;
    --card-black: #000000;
    --card-white: #ffffff;
    --accent-orange: #f0782a;
    --accent-orange-deep: #c9541b;
    --logo-silver: #d8d8d8;
    --ink-light: #ffffff;
    --ink-dark: #1a1a1a;
  }
  html, body {
    margin: 0;
    padding: 0;
    overflow: hidden;
  }
  .canvas {
    position: relative;
    width: 1200px;
    height: 900px;
    background: var(--backdrop);
    font-family: "Arimo", Arial, sans-serif;
    overflow: hidden;
  }
  .business-card {
    position: absolute;
    left: 252px;
    top: 242px;
    width: 698px;
    height: 418px;
    display: flex;
    background: var(--card-white);
  }
  .card-brand-panel {
    position: relative;
    width: 344px;
    height: 100%;
    background: var(--card-black);
  }
  .accent-stripe {
    width: 8px;
    height: 100%;
    background: linear-gradient(to bottom, var(--accent-orange), var(--accent-orange-deep));
  }
  .card-contact-panel {
    position: relative;
    flex: 1;
    height: 100%;
    background: var(--card-white);
  }
  .brand-mark {
    position: absolute;
    left: 34px;
    top: 108px;
    display: flex;
    align-items: center;
    gap: 12px;
  }
  .brand-dot {
    width: 20px;
    height: 20px;
    border-radius: 50%;
    background: var(--accent-orange);
  }
  .brand-name {
    font-weight: 700;
    font-size: 28px;
    color: var(--logo-silver);
    letter-spacing: 0.5px;
  }
  .holder {
    position: absolute;
    right: 28px;
    top: 256px;
    text-align: right;
    color: var(--ink-light);
  }
  .holder-name {
    font-size: 25px;
    line-height: 28px;
  }
  .holder-title {
    font-size: 19px;
    line-height: 26px;
  }
  .contact-list {
    position: absolute;
    left: 20px;
    top: 258px;
    margin: 0;
    padding: 0;
    list-style: none;
    color: var(--ink-dark);
    font-size: 16px;
    line-height: 22.5px;
    white-space: nowrap;
  }
</style>
</head>
<body>
  <div class="canvas">
    <section class="business-card">
      <div class="card-brand-panel">
        <div class="brand-mark">
          <span class="brand-dot"></span>
          <span class="brand-name">Kestrel Builders</span>
        </div>
        <div class="holder">
          <div class="holder-name">your nameixiox</div>
          <div class="holder-title">Director</div>
        </div>
      </div>
      <div class="accent-stripe"></div>
      <div class="card-contact-panel">
        <ul class="contact-list">
          <li>PO Box 5867, Wendara, NSW, 2487</li>
          <li>ABN &nbsp;: &nbsp;47 305 961 220</li>
          <li>BAS LIC 2650874</li>
          <li>Ph &nbsp;: &nbsp;07 3562 4470</li>
          <li>Fax : &nbsp;07 3562 4475</li>
          <li>Email : kestrelbuilders@mailbrook.com.au</li>
        </ul>
      </div>
    </section>
  </div>
</body>
</html>
```